Website for Youth Orchestra to sell tickets and attract young musicians

We are looking for a new website design for a Youth Orchestra; one of the best classical youth orchestras in the county. This project is the design only. <br/><br/>The website serves two main purposes:<br/>• Selling tickets for concerts and performances of the orchestra<br/>• Recruiting young musicians to do audition for the orchestra<br/>
Updates

Target Market(s)

Classical music lovers with a special interest in young upcoming musicians.
Young talented musicians

Number of Pages Required

2 page

Colors
ec1f27

Requirements
Must have
• - A Picture on the front page that promotes the main upcomming event
• - Attention for recruiting new musicians
• - Pictures with young musicians (white back ground, see examples)
• - Responsive
• - Please use the logo attached
Should not have
• The brown colors of the current website (kvb-veldhorst.example)

```html
<!DOCTYPE html>
<html lang="nl">
<head>
<meta charset="utf-8">
<title>Eemstad Jeugd Orkest</title>
<link rel="stylesheet" href="https://fonts.googleapis.com/css2?family=Pathway+Gothic+One&family=Montserrat:wght@300;400;500&display=swap">
<style>
:root{
  --red:#e31e2d;
  --red-dark:#b7141f;
  --pink:#f4a7aa;
  --pink-light:#fbe0e1;
  --pink-mid:#ee6a72;
  --grey-light:#f1f1f1;
  --text:#444;
  --muted:#777;
  --white:#fff;
}
*{margin:0;padding:0;box-sizing:border-box}
html,body{width:1200px;height:3861px;overflow:hidden;background:var(--white)}
body{position:relative;font-family:'Montserrat',sans-serif;color:var(--text)}
.abs{position:absolute}
.display{font-family:'Pathway Gothic One',sans-serif;font-weight:400}
.circle{position:absolute;border-radius:50%}

/* header */
.brand{left:39px;top:48px;width:129px;height:129px;border-radius:50%;background:var(--red);color:var(--white);display:flex;align-items:center;justify-content:center;text-align:center;font-family:'Pathway Gothic One',sans-serif;font-size:21px;line-height:1.05;z-index:3}
.social{top:30px;display:flex;gap:30px;left:730px;z-index:3}
.social span{width:20px;height:20px;border-radius:50%;background:var(--red);display:block}
.search{left:930px;top:26px;width:178px;height:28px;border:1px solid #ccc;border-radius:14px;font-size:10px;color:#999;padding:7px 16px;z-index:3}
.search svg{position:absolute;right:10px;top:6px}
.nav{top:104px;left:505px;width:605px;display:flex;justify-content:space-between;font-size:11.5px;letter-spacing:.5px;color:#333;z-index:3}

/* hero */
.hero{left:0;top:0;width:1200px;height:628px;overflow:hidden}
.hero h1{left:104px;top:258px;font-size:64px;line-height:54px;color:var(--red);z-index:2}
.hero p{left:104px;top:398px;font-size:22px;line-height:28px;color:var(--red);font-weight:300;width:460px;z-index:2}
.btn{position:absolute;border:2px solid var(--red);border-radius:40px;color:var(--red);display:flex;align-items:center;justify-content:center;font-weight:400}
.btn-hero{left:104px;top:497px;width:226px;height:57px;font-size:24px;z-index:2}

/* feature cards */
.card{position:absolute;top:644px;height:440px;overflow:hidden}
.card .photo{z-index:1}
.card h2{position:absolute;left:20px;top:105px;font-size:42px;line-height:41px;color:var(--red);z-index:2;white-space:nowrap}
.card .btn{left:12px;top:254px;width:132px;height:39px;font-size:14px;border-radius:6px;z-index:2;background:var(--white)}
.card-ticket{left:16px;width:382px;background:var(--red)}
.card-ticket h2{color:var(--white)}
.card-ticket .btn{border-color:var(--white);color:var(--white);left:19px;background:transparent}
.photo{position:absolute}

/* about */
.about-title{left:0;width:1200px;top:1170px;text-align:center;font-size:30px;font-weight:300;color:#333}
.about-title em{font-style:normal;color:var(--red)}
.about-text{left:255px;width:690px;top:1265px;text-align:center;font-size:16.5px;line-height:33px;font-weight:300;color:#555;z-index:2}
.video{left:272px;top:1541px;width:545px;height:344px;border-radius:10px;overflow:hidden;background:linear-gradient(135deg,#3a2412,#6b3b1c 50%,#2b1a0f);z-index:2}
.video-title{position:absolute;left:190px;top:20px;color:var(--white);font-family:'Pathway Gothic One',sans-serif;font-size:28px;white-space:nowrap}

/* events & categories */
.section-title{font-size:44px;color:var(--red)}
.event{position:absolute;left:272px;width:320px}
.event h3{font-family:'Pathway Gothic One',sans-serif;font-weight:400;font-size:21px;color:#222}
.event time{display:block;font-size:13px;color:var(--muted);margin-top:2px}
.event .rule{height:2px;background:#eee;margin-top:14px}
.event .tag{display:inline-block;margin-top:6px;background:var(--red);color:var(--white);font-size:11px;padding:2px 12px;width:67px}
.event .tag.closed{background:#666;width:74px}
.event svg{position:absolute;right:0;top:8px}
.event.past h3,.event.past time{color:#888}
.cat{position:absolute;left:690px}
.cat h3{font-family:'Pathway Gothic One',sans-serif;font-weight:400;font-size:22px;color:var(--red)}
.cat p{font-size:13px;color:var(--muted);margin-top:2px}

/* news */
.news{position:absolute;top:2782px;width:320px}
.news .photo{position:static;width:320px;height:214px}
.news h3{font-family:'Pathway Gothic One',sans-serif;font-weight:400;font-size:21px;color:#222;margin-top:36px}
.news p{font-size:12.5px;line-height:22.5px;color:var(--muted);margin-top:14px;font-weight:300}
.btn-more{left:535px;top:3252px;width:132px;height:40px;font-size:15px}

/* footer */
.footer{left:0;top:3452px;width:1200px;height:313px;background:var(--red)}
.footer-col{position:absolute;top:72px}
.footer-col h4{font-family:'Pathway Gothic One',sans-serif;font-weight:400;font-size:22px;color:var(--white);margin-bottom:12px}
.footer-col li{list-style:none;font-size:13.5px;color:#fbd0d2;line-height:31px;font-weight:300}
.copyright{left:0;top:3765px;width:1200px;height:96px;background:var(--red-dark);color:#f08a90;font-size:11px;text-align:center;padding-top:43px;font-weight:300}
</style>
</head>
<body>

<header>
  <div class="brand abs">Eemstad<br>Jeugd<br>Orkest</div>
  <div class="social abs" aria-label="Sociale media"><span></span><span></span><span></span></div>
  <div class="search abs">Site Zoeken...
    <svg width="16" height="16" viewBox="0 0 16 16"><circle cx="9.5" cy="6.5" r="5" fill="none" stroke="#e31e2d" stroke-width="1.5"/><line x1="6" y1="10" x2="1.5" y2="14.5" stroke="#e31e2d" stroke-width="1.5"/></svg>
  </div>
  <nav class="nav abs"><span>HOME</span><span>NIEUWS</span><span>OVER</span><span>ORKEST</span><span>CONCERTEN</span><span>AUDITIES</span><span>CONTACT</span></nav>
</header>

<section class="hero abs">
  <div class="circle" style="left:630px;top:105px;width:540px;height:540px;background:var(--pink-light)"></div>
  <div class="circle" style="left:510px;top:365px;width:380px;height:380px;background:var(--pink)"></div>
  <div class="circle" style="left:546px;top:208px;width:120px;height:120px;background:var(--pink-light)"></div>
  <div class="circle" style="left:930px;top:400px;width:248px;height:248px;background:var(--red)"></div>
  <div class="circle" style="left:928px;top:104px;width:84px;height:84px;background:var(--pink);opacity:.85"></div>
  <div class="circle" role="img" aria-label="Foto van een jong meisje dat viool speelt" style="left:702px;top:182px;width:382px;height:382px;background:radial-gradient(circle at 55% 40%,#e9c9a8,#9b5a2c 60%,#3d2413)"></div>
  <h1 class="abs display">kaartverkoop<br>nieuwjaars concert gestart!</h1>
  <p class="abs">Bekijk het laatste schema en ontdek hoe u uw stoelen kunt boeken</p>
  <a class="btn btn-hero">Leren meer</a>
</section>

<section>
  <div class="card card-ticket">
    <h2 class="display">Ticket<br>Reserving</h2>
    <a class="btn">Leren meer</a>
    <div class="photo" role="img" aria-label="Foto van een concertzaal met orgel en orkest" style="left:201px;top:0;width:181px;height:440px;background:linear-gradient(180deg,#6a3b16,#a8692e 40%,#3a1f0c)"></div>
  </div>
  <div class="card" style="left:410px;width:381px;background:var(--grey-light)">
    <div class="photo" role="img" aria-label="Foto van een juichend meisje met viool" style="left:160px;top:0;width:221px;height:440px;background:linear-gradient(180deg,#efe7e2,#d9a98a 55%,#b8652a)"></div>
    <h2 class="display">wat is<br>jeugd<br>orkest?</h2>
    <a class="btn">Leren meer</a>
  </div>
  <div class="card" style="left:805px;width:382px;background:var(--grey-light)">
    <div class="photo" role="img" aria-label="Foto van jonge musici in het zwart met instrumenten" style="left:170px;top:20px;width:212px;height:420px;background:linear-gradient(180deg,#f1f1f1,#b5b5b5 30%,#333 65%,#555)"></div>
    <h2 class="display">lid worden<br>van het<br>orkest</h2>
    <a class="btn">Inschrijven</a>
  </div>
</section>

<section>
  <h2 class="about-title abs">Over het <em>Eemstad</em> Jeugd Orkest</h2>
  <p class="about-text abs">Het Eemstad Jeugd Orkest (EJO) is een jeugdorkest dat in een volledig symfonische bezetting speelt. Het orkest repeteert elke vrijdagavond in de Sint-Lucaskerk in Eemstad. Deze repetitie is openbaar toegankelijk en we willen graag dat je met ons meedoet.</p>

  <div class="circle" style="left:510px;top:1425px;width:404px;height:404px;background:var(--grey-light)"></div>
  <div class="circle" style="left:118px;top:1488px;width:300px;height:300px;background:var(--pink)"></div>
  <div class="circle" style="left:478px;top:1740px;width:284px;height:284px;background:var(--pink-mid)"></div>
  <div class="circle" style="left:530px;top:1350px;width:134px;height:134px;background:var(--pink);opacity:.75"></div>
  <div class="circle" style="left:900px;top:1632px;width:96px;height:96px;background:var(--pink-mid)"></div>

  <div class="video abs" role="img" aria-label="Video van het orkest op het podium">
    <div class="video-title">EJO in de Stadsconcertzaal</div>
    <svg class="abs" style="left:460px;top:17px" width="60" height="40" viewBox="0 0 60 40"><circle cx="20" cy="20" r="19" fill="#fff"/><circle cx="20" cy="16" r="4" fill="none" stroke="#e31e2d" stroke-width="2"/><path d="M13 28a7 6 0 0 1 14 0" fill="none" stroke="#e31e2d" stroke-width="2"/><circle cx="53" cy="12" r="2.5" fill="#fff"/><circle cx="53" cy="20" r="2.5" fill="#fff"/><circle cx="53" cy="28" r="2.5" fill="#fff"/></svg>
    <svg class="abs" style="left:235px;top:141px" width="74" height="62" viewBox="0 0 74 62"><rect width="74" height="62" rx="14" fill="#e8e8e8"/><path d="M29 19 L50 31 L29 43Z" fill="#222"/></svg>
  </div>
  <div class="abs" role="img" aria-label="Illustratie van een cello" style="left:822px;top:1600px;width:178px;height:410px;border-radius:80px 80px 70px 70px;background:linear-gradient(160deg,#6a3a14,#b4722e 50%,#5a2d0c);z-index:2"></div>
  <div class="abs" style="left:840px;top:1985px;width:160px;height:30px;border-radius:50%;background:#e9e9e9"></div>
</section>

<section>
  <h2 class="section-title display abs" style="left:272px;top:2140px">Evenementenplanning</h2>
  <div class="event" style="top:2234px">
    <h3>Sint-Lucaskerk, Eemstad</h3><time>February 15, 2020 8:00 PM</time>
    <svg width="16" height="28" viewBox="0 0 16 28"><path d="M2 2 L14 14 L2 26" fill="none" stroke="#e31e2d" stroke-width="2.5"/></svg>
    <div class="rule"></div><span class="tag">Open</span>
  </div>
  <div class="event" style="top:2352px">
    <h3>Sint-Lucaskerk, Eemstad</h3><time>February 10, 2020 8:00 PM</time>
    <svg width="16" height="28" viewBox="0 0 16 28"><path d="M2 2 L14 14 L2 26" fill="none" stroke="#e31e2d" stroke-width="2.5"/></svg>
    <div class="rule"></div><span class="tag">Open</span>
  </div>
  <div class="event past" style="top:2477px">
    <h3>Sint-Lucaskerk, Eemstad</h3><time>January 1, 2020 8:00 PM</time>
    <svg width="16" height="28" viewBox="0 0 16 28"><path d="M2 2 L14 14 L2 26" fill="none" stroke="#888" stroke-width="2.5"/></svg>
    <div class="rule"></div><span class="tag closed">Gesloten</span>
  </div>

  <h2 class="section-title display abs" style="left:690px;top:2140px">Populaire Categorieën</h2>
  <div class="cat" style="top:2234px"><h3>Ticketaankoop</h3><p>Lorem Ipsum dolor Sit Amit</p></div>
  <div class="cat" style="top:2296px"><h3>Audities</h3><p>Lorem Ipsum dolor Sit Amit</p></div>
  <div class="cat" style="top:2358px"><h3>Tours &amp; Concerten</h3><p>Lorem Ipsum dolor Sit Amit</p></div>
  <div class="cat" style="top:2427px"><h3>Orkest</h3><p>Lorem Ipsum dolor Sit Amit</p></div>
</section>

<section>
  <h2 class="section-title display abs" style="left:272px;top:2682px">Laatste Nieuws &amp; Verhalen</h2>
  <article class="news" style="left:272px">
    <div class="photo" role="img" aria-label="Foto van een concert in een zaal met blauw licht" style="background:linear-gradient(180deg,#5b4a7a,#2d2fa8 55%,#1b1c5c)"></div>
    <h3>Concert Vogelaar met Bram Zijlstra</h3>
    <p>O, het is al weer even geleden, juni 2017 om precies te zijn. Het Vogelaar Zomerconcert bij Huize Eikenhof in Heidedorp. Zo'n bijzondere plek. We speelden onder andere romantische klassiekers...</p>
  </article>
  <article class="news" style="left:610px">
    <div class="photo" role="img" aria-label="Zwart-witfoto van een musicus met een cellokop" style="background:linear-gradient(90deg,#9a9a9a,#d6d6d6 45%,#222)"></div>
    <h3 style="margin-left:10px">Joris van Dijk is oud - EJO lid.</h3>
    <p style="margin-left:10px">Joris van Dijk is oud-EJO lid. Hij verliet ons orkest 13 jaar geleden om een professionele loopbaan als klassiek musicus te vervolgen. Vandaag geeft hij een bijzonder lunchconcert...</p>
  </article>
  <a class="btn btn-more">Meer laden</a>
</section>

<footer>
  <div class="footer abs">
    <div class="footer-col" style="left:288px"><h4>OVER ONS</h4><ul><li>Wat is jeugdorkest</li><li>Geschiedenis</li><li>Leden</li><li>Privacybeleid</li></ul></div>
    <div class="footer-col" style="left:497px"><h4>LID WORDEN</h4><ul><li>Auditie proces</li><li>Locaties</li><li>Verkiesbaarheid</li></ul></div>
    <div class="footer-col" style="left:722px"><h4>CONTACT OP</h4><ul><li>support@kvb-veldhorst.example</li><li>Eemstad Jeugd Orkest</li><li>Postbus 412</li><li>1234 AB Eemstad</li></ul></div>
  </div>
  <div class="copyright abs">Copyright 2020, dolor sit amet, consectetuer adipiscing elit, sed diam nonummy nibh euismod</div>
</footer>

</body>
</html>
```